Clean professional design needed for landscape property business

We need a logo for a new lawncare, landscaping , property maintenance business called Fernway Grove.
Our services include lawn mowing, garden maintenance, clean ups and some property maintenance.
We want a double sided business card that is clean and very professional using the colour scheme from our logo which is provided.
the business card should have impact as we will use these to drop into people's letterboxes as a marketing drop.
Initially we want to see what you come up with so there is a very wide scope here to work with.

Project Deadline Extended
Reason: we feel our original deadline was too short. we have extended to give more time for quality submissions.

Target Market(s)

High end property owners who don't wish to do there own gardneing or property maintenance

Industry/Entity Type

Business

Contact Information for Business Card

Name
Postion/ Title
Phone number
mobile
web address
physical address

services offered

Font styles to use
Sans Serif

Requirements
Must have
• curved edges preferrred
Nice to have
• We like the idea of the logo being embossed or etched into the card so it looks like it is below the surface of the card
Should not have
• No stock images or characters.

```html
<!DOCTYPE html>
<html lang="en">
<head>
<meta charset="utf-8">
<title>Fernway Grove – Business Card</title>
<link rel="stylesheet" href="https://fonts.googleapis.com/css2?family=Source+Sans+3:wght@400;600;700&display=swap">
<style>
  :root {
    --backdrop: #9a9a9a;
    --card-light: #f2f2f2;
    --card-dark: #222222;
    --leaf-green: #7dbb00;
    --ink: #3a3a3a;
    --slate: #55565a;
    --white: #ffffff;
    --rule: #8a8a8a;
  }
  * { box-sizing: border-box; margin: 0; padding: 0; }
  html, body {
    width: 1200px; height: 900px; overflow: hidden;
    background: var(--backdrop);
    font-family: "Source Sans 3", "Myriad Pro", Arial, sans-serif;
  }
  .canvas { position: relative; width: 1200px; height: 900px; }

  .card { position: absolute; top: 200px; width: 310px; height: 502px; }
  .card--front {
    left: 280px; background: var(--card-light);
    border-radius: 56px 0 56px 0;
  }
  .card--back {
    left: 626px; background: var(--card-dark);
    border-radius: 0 56px 0 56px;
  }

  /* Front */
  .brand-block {
    position: absolute; left: 60px; top: 90px; width: 190px;
    display: flex; align-items: center; gap: 12px;
  }
  .brand-block__square { width: 42px; height: 42px; background: var(--slate); flex: none; }
  .brand-block__name {
    color: var(--leaf-green); font-weight: 700; font-size: 30px; line-height: 1.0;
  }
  .person { position: absolute; left: 29px; top: 278px; }
  .person__name { color: var(--leaf-green); font-weight: 600; font-size: 18px; line-height: 22px; }
  .person__title { color: var(--ink); font-size: 14px; line-height: 18px; }

  .contact-list { position: absolute; left: 29px; top: 334px; list-style: none; }
  .contact-list li {
    display: flex; align-items: center; gap: 7px;
    color: var(--ink); font-size: 14px; line-height: 18px;
  }
  .contact-list svg { width: 10px; height: 10px; fill: var(--leaf-green); flex: none; }

  .address { position: absolute; left: 29px; top: 405px; color: var(--ink); font-size: 14px; line-height: 18px; }

  /* Back */
  .services { position: absolute; left: 0; right: 0; top: 119px; text-align: center; }
  .services__heading { font-size: 17px; font-weight: 600; color: var(--white); letter-spacing: 0.2px; }
  .services__heading span { color: var(--leaf-green); }
  .services__rule { width: 76px; height: 1px; background: var(--rule); margin: 13px auto 14px; }
  .services__list { list-style: none; }
  .services__list li {
    color: var(--white); font-size: 16px; line-height: 22.5px;
    display: flex; justify-content: center; align-items: center; gap: 7px;
  }
  .services__list li::before {
    content: ""; width: 7px; height: 7px; background: var(--leaf-green); flex: none;
  }

  .wordmark {
    position: absolute; left: 26px; top: 388px;
    display: flex; align-items: center; gap: 14px;
  }
  .wordmark__name { color: var(--leaf-green); font-weight: 700; font-size: 33px; letter-spacing: -1px; }
  .wordmark__square { width: 13px; height: 13px; background: var(--white); }
</style>
</head>
<body>
<main class="canvas">
  <section class="card card--front">
    <div class="brand-block">
      <div class="brand-block__square"></div>
      <div class="brand-block__name">Fernway<br>Grove</div>
    </div>

    <div class="person">
      <p class="person__name">Daniel Hart</p>
      <p class="person__title">Project Manager</p>
    </div>

    <ul class="contact-list">
      <li>
        <svg viewBox="0 0 10 10" aria-hidden="true"><path d="M2 0.5 L3.6 2.6 L2.7 3.6 C3.3 5 4.8 6.6 6.3 7.3 L7.4 6.4 L9.5 8 L8.4 9.5 C4.6 9.2 0.8 5.4 0.5 1.6 Z"/></svg>
        0198765432
      </li>
      <li>
        <svg viewBox="0 0 10 10" aria-hidden="true"><path d="M0.5 2 H9.5 V8.5 H0.5 Z M1.3 2.6 L5 5.4 L8.7 2.6" stroke="#f2f2f2" stroke-width="0.8"/></svg>
        info@fernwaygrove.com
      </li>
      <li>
        <svg viewBox="0 0 10 10" aria-hidden="true"><circle cx="5" cy="5" r="4.5"/></svg>
        www.fernwaygrove.com
      </li>
    </ul>

    <p class="address">Address Line1, Address Line2<br>Country - 12456</p>
  </section>

  <section class="card card--back">
    <div class="services">
      <h2 class="services__heading"><span>SERVICES</span> OFFERED</h2>
      <div class="services__rule"></div>
      <ul class="services__list">
        <li>Lawn mowing</li>
        <li>Garden maintenance</li>
        <li>Clean ups</li>
        <li>Property maintenance.</li>
      </ul>
    </div>

    <div class="wordmark">
      <span class="wordmark__name">fernwaygrove</span>
      <span class="wordmark__square"></span>
    </div>
  </section>
</main>
</body>
</html>
```